Price list for young Relaxon clinic

I require a price list/Treatment menu for clinic

To include:
Logo
Address
Phone number
Website

List of services and Prices
Relaxon 1 area £100
Relaxon 2 areas £150
Relaxon 3 areas £200
Lip Enhancement 0.5ml £100
Lip Enhancement 1ml £200
Facial Fillers £200 per 1ml
Volumiq £450 per session (2 vials - must be bought as a course)
Non Surgical Face Lift (Thread Lift) £600 per area
Skin Press Full Face £250
Skin Press Small Per Small Area £100
Cryo Therapy £60
Chemical Peel Light Peel and Microdermabrasion £85
Chemical Peel Deep Peel £150
Consultation £30 redeemable against service
Relaxon Top Up Relaxon £50 (must be within 2 weeks of 1st treatment)
Filler Top Up £100 (must be within 2 weeks of 1st appointment)

Open Hours
Updates

Company Name: HVM Address: 482 Pellbrook Road, 6 Warnford High Street, KT4 3JQ Phone: 0208 947 2186 Website: www.hollyvanmereaesthetics.co.uk

Please add more colour

Needs to be much cleaner and simpler Front page to include logo and price list Back page to inculde open hours and contact information including google map. Please no images with needles. Images of lips and faces are good, but try not to crowd copy on the pagei. No copy on top of images. White, grey, black and reds are good on colouring.

Target Market(s)

young market ages 22-45 years old mainly female
modern

Industry/Entity Type

Clinic

Number of Pages Required

4 page

Requirements
Must have
• Logo - logo must be in colour grey/silver
• Address (small map?)
• Phone number
• Web address
• Services
• Open hours
• Prices
• Images

```html
<!DOCTYPE html>
<html lang="en">
<head>
<meta charset="utf-8">
<title>Holly Vanmere Aesthetics – Treatment Menu</title>
<link rel="stylesheet" href="https://fonts.googleapis.com/css2?family=Cinzel:wght@400;700&family=Crimson+Pro:ital,wght@0,400;0,600;0,700;1,400&family=Pinyon+Script&display=swap">
<style>
  :root {
    --backdrop: #e8c6b1;
    --paper: #e2e2df;
    --logo-grey: #9b9b9b;
    --ink: #2b2b2b;
    --ink-soft: #4a4a4a;
    --muted: #a3a3a3;
    --rule: #8f8f8f;
    --photo-dark: #5c5656;
    --photo-light: #d9d6d4;
    --accent: #b98a6c;
  }
  * { box-sizing: border-box; margin: 0; padding: 0; }
  html, body { width: 1200px; height: 960px; overflow: hidden; }
  body {
    background: var(--backdrop);
    font-family: "Crimson Pro", Georgia, serif;
    color: var(--ink);
    position: relative;
  }
  .page {
    position: absolute;
    top: 98px;
    width: 540px;
    height: 764px;
    background: var(--paper);
    box-shadow: 0 4px 14px rgba(0,0,0,0.18);
  }
  .page--front { left: 40px; }
  .page--back { left: 620px; }

  .brand { position: absolute; left: 0; right: 0; text-align: center; }
  .brand__mark {
    display: block; margin: 0 auto;
    border-radius: 50%;
    background: var(--logo-grey);
  }
  .brand__name {
    font-family: "Cinzel", "Times New Roman", serif;
    font-weight: 400;
    color: var(--logo-grey);
    letter-spacing: 2px;
    line-height: 1.05;
  }
  .page--front .brand { top: 36px; }
  .page--front .brand__mark { width: 74px; height: 74px; margin-bottom: 14px; }
  .page--front .brand__name { font-size: 27px; }
  .page--back .brand { top: 40px; }
  .page--back .brand__mark { width: 58px; height: 58px; margin-bottom: 12px; }
  .page--back .brand__name { font-size: 22px; }

  .side-rule {
    position: absolute; height: 0;
    border-top: 1px solid var(--muted);
  }

  .hero-photo {
    position: absolute;
    left: 60px; top: 212px;
    width: 420px; height: 370px;
    background: radial-gradient(ellipse at 50% 40%, var(--photo-light) 0%, #b9b4b1 45%, var(--photo-dark) 100%);
  }

  .tagline {
    position: absolute; left: 0; right: 0; top: 598px;
    text-align: center;
    font-family: "Pinyon Script", cursive;
    font-size: 34px;
    color: var(--ink);
  }
  .contact-rule {
    position: absolute; left: 120px; right: 120px; top: 650px;
    border-top: 1px solid var(--muted);
  }
  .contact {
    position: absolute; left: 0; right: 0; top: 660px;
    text-align: center;
  }
  .contact__phone { font-size: 30px; font-weight: 700; line-height: 1.1; }
  .contact__web { font-size: 20px; font-weight: 600; margin-top: 4px; }
  .contact__social { font-size: 20px; font-weight: 600; margin-top: 2px; display: flex; justify-content: center; align-items: center; gap: 6px; }
  .contact__social-square { width: 14px; height: 14px; background: var(--ink); display: inline-block; }

  .price-list {
    position: absolute; left: 34px; right: 34px; top: 176px;
  }
  .price-list__head {
    display: grid; grid-template-columns: 1fr 250px;
    font-weight: 700; font-size: 16px; letter-spacing: 1px;
    padding-bottom: 3px;
    border-bottom: 1.5px solid var(--ink-soft);
  }
  .price-row {
    display: grid; grid-template-columns: 1fr 250px;
    align-items: center;
    font-size: 15px; line-height: 1.15;
    padding: 3px 0;
    border-bottom: 1px solid var(--rule);
    min-height: 24px;
  }
  .price-row__note { display: block; font-style: italic; font-size: 12px; }
  .price-row em { font-size: 13px; }

  .footer-rule {
    position: absolute; left: 34px; right: 34px; top: 610px;
    border-top: 1px solid var(--muted);
  }
  .hours, .address {
    position: absolute; top: 630px;
    color: var(--muted);
    font-size: 14px; line-height: 1.45;
  }
  .hours { left: 34px; width: 140px; }
  .address { left: 400px; width: 120px; }
  .info-title {
    font-weight: 700; font-size: 16px; letter-spacing: 1px;
    margin-bottom: 4px;
  }
  .hours strong { font-weight: 600; }
  .map-area {
    position: absolute; left: 180px; top: 624px;
    width: 208px; height: 116px;
    background: linear-gradient(135deg, #f1f1f0 0%, #d9d9d8 100%);
  }
</style>
</head>
<body>

<section class="page page--front">
  <div class="side-rule" style="left:14px; width:100px; top:192px;"></div>
  <div class="side-rule" style="right:14px; width:100px; top:192px;"></div>

  <header class="brand">
    <span class="brand__mark" aria-hidden="true"></span>
    <div class="brand__name">HVM<br>HOLLY VANMERE<br>AESTHETICS</div>
  </header>

  <div class="hero-photo" role="img" aria-label="Black and white collage of a woman's face framed by her hands, with close-up tiles of eyes and lips"></div>

  <p class="tagline">Achieve a fresh and beautiful you!</p>
  <div class="contact-rule"></div>

  <div class="contact">
    <div class="contact__phone">0208 947 2186</div>
    <div class="contact__web">www.hollyvanmereaesthetics.co.uk</div>
    <div class="contact__social"><span class="contact__social-square" aria-hidden="true"></span>hollyvanmereaesthetics</div>
  </div>
</section>

<section class="page page--back">
  <div class="side-rule" style="left:0; width:60px; top:70px;"></div>
  <div class="side-rule" style="right:0; width:60px; top:110px;"></div>

  <header class="brand">
    <span class="brand__mark" aria-hidden="true"></span>
    <div class="brand__name">HVM<br>HOLLY VANMERE<br>AESTHETICS</div>
  </header>

  <div class="price-list">
    <div class="price-list__head"><span>TREATMENTS</span><span>PRICES</span></div>
    <div class="price-row"><span>Relaxon 1 area</span><span>£100</span></div>
    <div class="price-row"><span>Relaxon 2 areas</span><span>£150</span></div>
    <div class="price-row"><span>Relaxon 3 areas</span><span>£200</span></div>
    <div class="price-row"><span>Lip Enhancement 0.5ml</span><span>£100</span></div>
    <div class="price-row"><span>Lip Enhancement 1ml</span><span>£200</span></div>
    <div class="price-row"><span>Facial Fillers</span><span>£200 per 1ml</span></div>
    <div class="price-row"><span>Volumiq</span><span>£450 per session<span class="price-row__note">(2 vials - must be bought as a course)</span></span></div>
    <div class="price-row"><span>Non Surgical Face Lift (Thread Lift)</span><span>£600 per area</span></div>
    <div class="price-row"><span>Skin Press Full Face</span><span>£250</span></div>
    <div class="price-row"><span>Skin Press Small Per Small Area</span><span>£100</span></div>
    <div class="price-row"><span>Cryo Therapy</span><span>£60</span></div>
    <div class="price-row"><span>Chemical Peel Light Peel<br>and Microdermabrasion</span><span>£85</span></div>
    <div class="price-row"><span>Chemical Peel Deep Peel</span><span>£150</span></div>
    <div class="price-row"><span>Consultation</span><span>£30 <em>redeemable against service</em></span></div>
    <div class="price-row"><span>Top Up Relaxon</span><span>£50 <em>(must be within 2 weeks of 1st treatment)</em></span></div>
    <div class="price-row"><span>Filler Top Up</span><span>£100 <em>(must be within 2 weeks of 1st appointment)</em></span></div>
  </div>

  <div class="footer-rule"></div>

  <div class="hours">
    <div class="info-title">OPENING TIMES</div>
    <div><strong>Mon–Fri:</strong> 10am – 7pm</div>
    <div><strong>Sat:</strong> 10am – 4pm</div>
    <div><em>(appointments only)</em></div>
    <div><strong>Sun:</strong> Closed</div>
  </div>

  <div class="map-area" role="img" aria-label="Street map showing the clinic location on Warnford Parade"></div>

  <div class="address">
    <div class="info-title">ADDRESS</div>
    <div>6 Warnford Parade</div>
    <div>Surrey</div>
    <div>KT4 3JQ</div>
  </div>
</section>

</body>
</html>
```